I need a label design for my up coming wine bottle

The bottle is a standard wine bottle, 720 ML. The label needs to be elegant 1-3 colors preferably with grape vines highlighting my winery name. 5-8 cellars

```html
<!DOCTYPE html>
<html lang="en">
<head>
<meta charset="utf-8">
<title>5-8 Cellars – Wine Label Set</title>
<link rel="stylesheet" href="https://fonts.googleapis.com/css2?family=Cormorant+Garamond:wght@600&family=Montserrat:wght@600&family=Oswald:wght@500&display=swap">
<style>
  :root {
    --page: #ffffff;
    --cream: #f4ebe1;
    --cream-light: #f3ebdb;
    --charcoal: #262626;
    --ink: #2b2223;
    --silver: #e2e2e2;
    --gold: #c99a4e;
    --gold-light: #e6c98c;
    --gold-deep: #a97a38;
    --serif: "Cormorant Garamond", Georgia, serif;
    --sans: "Montserrat", Arial, sans-serif;
    --condensed: "Oswald", "Arial Narrow", sans-serif;
  }
  * { box-sizing: border-box; margin: 0; padding: 0; }
  html, body { width: 1200px; height: 848px; overflow: hidden; background: var(--page); }
  .canvas { position: relative; width: 1200px; height: 848px; }

  /* Rectangular labels */
  .label-rect { position: absolute; top: 158px; width: 347px; height: 522px; }
  .label-rect--light { left: 51px; background: var(--cream); color: var(--ink); }
  .label-rect--dark { left: 449px; background: var(--charcoal); color: var(--silver); }
  .label-rect .frame { position: absolute; inset: 0; }
  .ornament-top, .ornament-bottom, .ornament-side {
    position: absolute;
    background: radial-gradient(ellipse at center, var(--gold-light), var(--gold) 70%);
    border-radius: 50%;
  }
  .ornament-top { left: 150px; top: 8px; width: 47px; height: 14px; }
  .ornament-bottom { left: 150px; top: 500px; width: 47px; height: 14px; }
  .ornament-side { top: 216px; width: 20px; height: 76px; }
  .ornament-side--left { left: 7px; }
  .ornament-side--right { right: 7px; }
  .vine-art {
    position: absolute; left: 110px; top: 36px; width: 128px; height: 147px;
    border-radius: 45% 45% 40% 40%;
  }
  .label-rect--light .vine-art { background: radial-gradient(ellipse at 50% 45%, #a9a4a0, #d8d1c8 75%); }
  .label-rect--dark .vine-art { background: radial-gradient(ellipse at 50% 50%, #b9ac7c, #57533f 80%); }
  .tagline {
    position: absolute; top: 154px; font-family: var(--sans); font-weight: 600; font-size: 13px;
    line-height: 1; letter-spacing: 3.8px; white-space: nowrap;
  }
  .tagline--left { left: 22px; }
  .tagline--right { left: 213px; }
  .label-rect--dark .tagline { color: #e8e8e8; }
  .brand-name { position: absolute; left: 0; width: 100%; text-align: center; font-family: var(--serif); font-weight: 600; line-height: 1; }
  .brand-name__number { display: block; font-size: 84px; }
  .brand-name__word { display: block; font-size: 66px; margin-top: -4px; }
  .label-rect .brand-name { top: 196px; }
  .vintage { position: absolute; top: 368px; width: 100%; text-align: center; font-family: var(--serif); font-weight: 600; font-size: 36px; line-height: 1; }
  .divider { position: absolute; left: 97px; top: 414px; width: 155px; height: 8px; }
  .specs { position: absolute; top: 430px; font-family: var(--serif); font-weight: 600; font-size: 20px; line-height: 1.2; letter-spacing: 1px; }
  .specs--alc { left: 57px; }
  .specs--vol { right: 63px; }

  /* Capsule label */
  .label-capsule {
    position: absolute; left: 908px; top: 97px; width: 171px; height: 272px;
    border-radius: 86px; border: 6px solid var(--gold);
    background: radial-gradient(ellipse at 50% 45%, #fbf6ec, var(--cream-light) 70%);
    color: var(--ink);
  }
  .label-capsule .arc-text { position: absolute; left: -6px; top: -6px; }
  .label-capsule .vine-art-small {
    position: absolute; left: 55px; top: 25px; width: 47px; height: 57px;
    border-radius: 40%; background: radial-gradient(ellipse, #9c9893, #ddd6cb 80%);
  }
  .small-specs { position: absolute; font-family: var(--serif); font-weight: 600; font-size: 10.5px; white-space: nowrap; }
  .label-capsule .small-specs { top: 66px; }
  .label-capsule .small-specs--alc { left: 10px; }
  .label-capsule .small-specs--vol { right: 6px; }
  .label-capsule .brand-name { top: 86px; }
  .label-capsule .brand-name__number { font-size: 44px; }
  .label-capsule .brand-name__word { font-size: 38px; margin-top: -2px; }
  .ribbon { position: absolute; left: 882px; top: 280px; width: 221px; height: 54px; }
  .since { position: absolute; width: 100%; text-align: center; font-family: var(--condensed); font-size: 9.5px; letter-spacing: 0.3px; }
  .label-capsule .since { top: 242px; }

  /* Arch label */
  .label-arch {
    position: absolute; left: 899px; top: 404px; width: 192px; height: 329px;
    border-radius: 96px 96px 0 0;
    background: linear-gradient(90deg, var(--gold-deep), #c99a58 45%, #c99a58 55%, var(--gold-deep));
    color: var(--ink);
  }
  .label-arch .inner-line {
    position: absolute; inset: 8px; border: 1px solid var(--ink); border-radius: 88px 88px 0 0;
  }
  .label-arch .arc-text { position: absolute; left: 0; top: 0; }
  .label-arch .vine-art-small {
    position: absolute; left: 56px; top: 43px; width: 81px; height: 92px;
    border-radius: 40%; background: radial-gradient(ellipse, #8a6a3c, #b88b4c 80%);
  }
  .label-arch .small-specs { top: 101px; }
  .label-arch .small-specs--alc { left: 20px; }
  .label-arch .small-specs--vol { right: 16px; }
  .label-arch .brand-name { top: 150px; }
  .label-arch .brand-name__number { font-size: 58px; }
  .label-arch .brand-name__word { font-size: 44px; margin-top: 0; }
  .label-arch .since { top: 296px; font-size: 11px; }
</style>
</head>
<body>
<main class="canvas">

  <!-- Light label -->
  <section class="label-rect label-rect--light">
    <svg class="frame" width="347" height="522" viewBox="0 0 347 522" aria-hidden="true">
      <path d="M33 14H314A17 17 0 0 0 331 31V491A17 17 0 0 0 314 508H33A17 17 0 0 0 16 491V31A17 17 0 0 0 33 14Z" fill="none" stroke="#c99a4e" stroke-width="1.3"/>
      <g fill="#c99a4e"><circle cx="18" cy="16" r="3"/><circle cx="329" cy="16" r="3"/><circle cx="18" cy="506" r="3"/><circle cx="329" cy="506" r="3"/></g>
    </svg>
    <div class="ornament-top" role="img" aria-label="Gold scroll ornament"></div>
    <div class="ornament-bottom" role="img" aria-label="Gold scroll ornament"></div>
    <div class="ornament-side ornament-side--left" role="img" aria-label="Gold side flourish"></div>
    <div class="ornament-side ornament-side--right" role="img" aria-label="Gold side flourish"></div>
    <div class="vine-art" role="img" aria-label="Engraved grape bunch with vine leaves"></div>
    <p class="tagline tagline--left">•PREMIUM•</p>
    <p class="tagline tagline--right">• QUALITY •</p>
    <h1 class="brand-name"><span class="brand-name__number">5-8</span><span class="brand-name__word">Cellars</span></h1>
    <p class="vintage">2023</p>
    <svg class="divider" viewBox="0 0 155 8" aria-hidden="true"><line x1="3" y1="4" x2="152" y2="4" stroke="#c99a4e" stroke-width="1.5"/><g fill="#c99a4e"><rect x="0" y="1.5" width="5" height="5" transform="rotate(45 2.5 4)"/><rect x="75" y="1.5" width="5" height="5" transform="rotate(45 77.5 4)"/><rect x="150" y="1.5" width="5" height="5" transform="rotate(45 152.5 4)"/></g></svg>
    <p class="specs specs--alc">ALC 11.5%</p>
    <p class="specs specs--vol">720ml</p>
  </section>

  <!-- Dark label -->
  <section class="label-rect label-rect--dark">
    <svg class="frame" width="347" height="522" viewBox="0 0 347 522" aria-hidden="true">
      <path d="M33 14H314A17 17 0 0 0 331 31V491A17 17 0 0 0 314 508H33A17 17 0 0 0 16 491V31A17 17 0 0 0 33 14Z" fill="none" stroke="#c99a4e" stroke-width="1.3"/>
      <g fill="#c99a4e"><circle cx="18" cy="16" r="3"/><circle cx="329" cy="16" r="3"/><circle cx="18" cy="506" r="3"/><circle cx="329" cy="506" r="3"/></g>
    </svg>
    <div class="ornament-top" role="img" aria-label="Gold scroll ornament"></div>
    <div class="ornament-bottom" role="img" aria-label="Gold scroll ornament"></div>
    <div class="ornament-side ornament-side--left" role="img" aria-label="Gold side flourish"></div>
    <div class="ornament-side ornament-side--right" role="img" aria-label="Gold side flourish"></div>
    <div class="vine-art" role="img" aria-label="Engraved gold grape bunch with vine leaves"></div>
    <p class="tagline tagline--left">•PREMIUM•</p>
    <p class="tagline tagline--right">• QUALITY •</p>
    <h2 class="brand-name"><span class="brand-name__number">5-8</span><span class="brand-name__word">Cellars</span></h2>
    <p class="vintage">2023</p>
    <svg class="divider" viewBox="0 0 155 8" aria-hidden="true"><line x1="3" y1="4" x2="152" y2="4" stroke="#c99a4e" stroke-width="1.5"/><g fill="#e6c98c"><rect x="0" y="1.5" width="5" height="5" transform="rotate(45 2.5 4)"/><rect x="75" y="1.5" width="5" height="5" transform="rotate(45 77.5 4)"/><rect x="150" y="1.5" width="5" height="5" transform="rotate(45 152.5 4)"/></g></svg>
    <p class="specs specs--alc">ALC 11.5%</p>
    <p class="specs specs--vol">720ml</p>
  </section>

  <!-- Capsule label -->
  <section class="label-capsule">
    <svg class="arc-text" width="171" height="90" viewBox="0 0 171 90" aria-hidden="true">
      <path id="capsule-arc" d="M26 80A60 60 0 0 1 146 80" fill="none"/>
      <text font-family="Cormorant Garamond, serif" font-weight="600" font-size="11.5" fill="#2b2223" letter-spacing="0.6"><textPath href="#capsule-arc" startOffset="50%" text-anchor="middle">PREMIUM QUALITY</textPath></text>
    </svg>
    <div class="vine-art-small" role="img" aria-label="Engraved grape bunch"></div>
    <p class="small-specs small-specs--alc">ALC 11.5%</p>
    <p class="small-specs small-specs--vol">VOL 720ml</p>
    <h2 class="brand-name"><span class="brand-name__number">5-8</span><span class="brand-name__word">Cellars</span></h2>
    <p class="since">SINCE 2023</p>
  </section>
  <svg class="ribbon" viewBox="0 0 221 54" aria-hidden="true">
    <path d="M2 38L14 28L8 20L30 16L28 42Z" fill="#a97a38"/>
    <path d="M219 38L207 28L213 20L191 16L193 42Z" fill="#a97a38"/>
    <path d="M12 8Q110 40 209 8L213 36Q110 70 8 36Z" fill="#efe2c9" stroke="#a97a38" stroke-width="1.5"/>
    <path id="ribbon-arc" d="M30 30Q110 58 192 30" fill="none"/>
    <text font-family="Cormorant Garamond, serif" font-weight="600" font-size="19" fill="#c99a4e" letter-spacing="1.5"><textPath href="#ribbon-arc" startOffset="50%" text-anchor="middle">COLLECTION</textPath></text>
  </svg>

  <!-- Arch label -->
  <section class="label-arch">
    <div class="inner-line"></div>
    <svg class="arc-text" width="192" height="100" viewBox="0 0 192 100" aria-hidden="true">
      <path id="arch-arc" d="M26 88A70 70 0 0 1 166 88" fill="none"/>
      <text font-family="Cormorant Garamond, serif" font-weight="600" font-size="12.5" fill="#2b2223" letter-spacing="0.6"><textPath href="#arch-arc" startOffset="50%" text-anchor="middle">PREMIUM QUALITY</textPath></text>
    </svg>
    <div class="vine-art-small" role="img" aria-label="Engraved grape bunch in bronze tones"></div>
    <p class="small-specs small-specs--alc">ALC 11.5%</p>
    <p class="small-specs small-specs--vol">VOL 720ml</p>
    <h2 class="brand-name"><span class="brand-name__number">5-8</span><span class="brand-name__word">Cellars</span></h2>
    <p class="since">SINCE 2023</p>
  </section>

</main>
</body>
</html>
```